Clean, simple text based poster for printing: Street names using nice fonts

Clean/simple/typography: Street names poster

I am looking for a designer to make a simple text-based poster (A4/A3 size)

Basically, my parents have lived in many different places and I am looking for a poster which (a) shows all the streetnames they have lived in and (b) highlights in some way the last streetname, which is where they will retire.

- I am looking for clean/simple design with nice fonts.
- I had in mind perhaps different sizes and orientation of text.
- The streetnames should fill the whole canvas in a "tetris-like" fashion
- The "final" street name should stand out
- Perhaps a light background color, or a background image of some sort ...
- A light frame around the design

but then again, I'm a scientist and not a designer which is why I am here... so feel free to let the creative juices flow :)

The street names
- Corriston Road
- Brantwell Avenue
- Kolvaripur Street
- Kelbstraße
- Wurmelring
- Dunhollow Avenue
- Rue des Brumeliers
- Rue de Vostremont
- Pilzmayergasse
- Kromvigs Allé
- Lipečka Ulica
- Quernbachstraße
- Wolkenmarstraße
- Allée du Doux Crépuscule (Final street)

Ned

```html
<!DOCTYPE html>
<html lang="en">
<head>
<meta charset="utf-8">
<title>Street Names Poster</title>
<link rel="stylesheet" href="https://fonts.googleapis.com/css2?family=Rokkitt:wght@400&display=swap">
<style>
  :root {
    --bg: #0f2b31;
    --street: #d2486c;
    --final: #9fcd7c;
  }
  html, body {
    margin: 0;
    padding: 0;
    width: 848px;
    height: 1200px;
    overflow: hidden;
    background: var(--bg);
  }
  .poster {
    display: block;
    width: 848px;
    height: 1200px;
    background: var(--bg);
  }
  .street-name {
    font-family: "Rokkitt", Georgia, serif;
    font-weight: 400;
    fill: var(--street);
  }
  .street-name--final {
    fill: var(--final);
  }
</style>
</head>
<body>
<svg class="poster" width="848" height="1200" viewBox="0 0 848 1200" xmlns="http://www.w3.org/2000/svg" role="img" aria-label="Poster listing street names, ending with Allée du Doux Crépuscule">
  <g class="street-list">
    <text class="street-name" x="64" y="125" font-size="45" textLength="713" lengthAdjust="spacing">·CORRISTON ROAD·</text>
    <text class="street-name" x="64" y="197" font-size="57" textLength="713" lengthAdjust="spacing">BRANTWELL AVENUE</text>
    <text class="street-name" x="64" y="269" font-size="57" textLength="713" lengthAdjust="spacing">KOLVARIPUR STREET</text>
    <text class="street-name" x="64" y="393" font-size="134" textLength="713" lengthAdjust="spacingAndGlyphs">KELBSTRAßE</text>
    <text class="street-name" x="64" y="465" font-size="57" textLength="713" lengthAdjust="spacingAndGlyphs">WURMELRING · DUNHOLLOW AVENUE</text>
    <text class="street-name" x="64" y="537" font-size="57" textLength="713" lengthAdjust="spacing">RUE DES BRUMELIERS</text>
    <text class="street-name" x="64" y="609" font-size="57" textLength="713" lengthAdjust="spacing">RUE DE VOSTREMONT</text>
    <text class="street-name" x="64" y="723" font-size="120" textLength="713" lengthAdjust="spacingAndGlyphs">PILZMAYERGASSE</text>
    <text class="street-name" x="64" y="795" font-size="57" textLength="713" lengthAdjust="spacing">KROMVIGS ALLÉ</text>
    <text class="street-name" x="64" y="901" font-size="93" textLength="713" lengthAdjust="spacingAndGlyphs">LIPEČKA ULICA</text>
    <text class="street-name" x="64" y="973" font-size="57" textLength="713" lengthAdjust="spacing">QUERNBACHSTRAßE</text>
    <text class="street-name" x="64" y="1037" font-size="45" textLength="713" lengthAdjust="spacing">·WOLKENMARSTRAßE·</text>
    <text class="street-name street-name--final" x="64" y="1115" font-size="66" textLength="713" lengthAdjust="spacingAndGlyphs">ALLÉE DU DOUX CRÉPUSCULE</text>
  </g>
</svg>
</body>
</html>
```